Brochure Design Project - Brelwick Motors Auto Repair Centre

We require a high quality brochure (A3 folded to A4) for us to send to local businesses to try and get more sales. We would like to keep our current colour scheme from our flyers. We are garagemark approved so we require this logo to be included in the design. The font used on our flyer is QuickLinesRG available from fontvault-example.com
This is a brief of the information we require on our brochure (the feedback from our current customers still to be received but it will be limited to 1 line each) :
Introduction to Brelwick Motors
Based in Cumbernauld, Brelwick Motors are a family run Auto service centre and believe in giving helpful, friendly expert advice in plain English. We have a wealth of experience in a wide range of vehicles and we invest heavily in equipment to ensure our work is completed to the highest possible quality standards.
It is our aim to deliver a quality service at competitive rates for our customers. We have just expanded by investing in a new 4000 sq/ft workshop to help support our ever expanding customer base.
Why are we the best choice for your business?
Choosing a garage for your business can be a tough decision. Who do you choose and who do you trust? Cost will of course be high on your list, so why take your car to a main dealer and pay main dealer prices?
• Brelwick Motors Cumbernauld can carry out servicing and repairs to main dealer standards without the high prices. We can also maintain your vehicles warranty by using genuine manufacturer's parts.
• Communication is key – we never leave you wondering when your vehicle is going to be returned. 98% of vehicles we maintain are returned the same day.
• We never carry out any work to a vehicle without prior agreement – so no unexpected bills. You always get a fully itemised VAT invoice.
• We can arrange payment terms that are suitable to both businesses.
• We have flexibility with our working hours to ensure your fleet stays on the road no matter how big or small.
• We also pride ourselves on providing a professional and efficient service, your vehicle will be looked after as if it was our own pride and joy.
How can we guarantee quality?
Garage mark is the Trading Standards code of practice for garages. We are the only independent garage in Cumbernauld to achieve this standard. We are audited to ensure we comply with the code at all times and we must follow a strict complaints procedure should the need arise.
All parts fitted are covered by a 3 month or 6000 mile warranty. *Does not include wear and tear
What services can we offer your business?
MOT Testing
Vehicle Servicing
Budget & Performance Tyres
Mechanical Repairs
Exhausts, DPF filters & CAT’s
Brake repair specialist
Same day Clutch repairs
Gearboxes
Starter motors
Alternators
Wheel Alignment
MOT Welding
Replacement Batteries
ECU Fault Diagnostics & Service resets
Collection and drop off services
We are comprehensively insured to drive all of our customers’ vehicles so we can collect vehicles at a time that suits you and deliver them back with minimal impact to your business. The only time we will ever drive your vehicles is during transportation or testing.
Our current business customers – testimonials
Pettigrew Roofing
Crest Fitting
Hollowbys
Ruvan Loader training
Sample price list
£74.17 for car service/small vans
£91.67 for commercials up to 3500kgs (class IV)
Mot’s £35 for cars and vans (class IV)
Tyre sample prices – Ford Focus £36.95, Renault Kangoo £32.45, Ford Transit £41.55.
Labour rate of £35.00ph
All prices exclude VAT at applicable rate, unless stated otherwise and are correct at time of printing. Subject to change without prior notice. No VAT on MOT's
Contact Us
Brelwick Motors can be contacted to discuss your individual requirement by -
Phone: 01236 482915
Email: sales@brelwick-example.co.uk
Mon – Fri 8.00am – 5.30pm
Sat – 8.00am – 4.00pm
Target Market(s)
local businesses
Industry/Entity Type
Garage
Requirements
Must have
- garagemark logo
brelwick motors logo

```html
<!DOCTYPE html>
<html lang="en">
<head>
<meta charset="utf-8">
<title>Brelwick Motors Brochure Cover</title>
<link href="https://fonts.googleapis.com/css2?family=Source+Sans+3:wght@300;400;600;700&display=swap" rel="stylesheet">
<style>
  :root {
    --backdrop: #2a2b2d;
    --brand-blue: #3a8af5;
    --brand-blue-deep: #1b57d8;
    --accent-yellow: #f7ee1b;
    --text-white: #ffffff;
    --photo-dark: #1c1c1c;
    --photo-mid: #6a6d72;
  }
  * { margin: 0; padding: 0; box-sizing: border-box; }
  html, body {
    width: 1200px; height: 683px; overflow: hidden;
    background: var(--backdrop);
    font-family: "Source Sans 3", "Myriad Pro", Arial, sans-serif;
  }
  .spread {
    position: absolute; left: 179px; top: 40px;
    width: 857px; height: 605px;
    display: flex;
    box-shadow: 0 4px 14px rgba(0,0,0,0.5);
  }
  .page { position: relative; width: 428.5px; height: 605px; background: var(--brand-blue); overflow: hidden; }

  /* Back page */
  .info-block { position: absolute; left: 61px; color: var(--text-white); }
  .hours { top: 326px; }
  .contact { top: 446px; }
  .location { top: 520px; }
  .info-title { font-size: 17px; font-weight: 300; line-height: 18px; }
  .info-label { color: var(--accent-yellow); font-size: 16px; font-weight: 700; line-height: 17px; }
  .info-line { font-size: 15px; font-weight: 300; line-height: 18px; }
  .info-note { font-size: 9px; font-weight: 400; line-height: 16px; }
  .info-small { font-size: 12.5px; font-weight: 300; line-height: 13px; }
  .detail-key { display: inline-block; width: 42px; }

  /* Front page */
  .cover-photo {
    position: absolute; left: 0; top: 0; width: 100%; height: 330px;
    background: radial-gradient(ellipse at 45% 40%, var(--photo-mid) 0%, #3b3d40 40%, var(--photo-dark) 100%);
  }
  .cover-shapes { position: absolute; left: 0; top: 0; }
  .selling-points {
    position: absolute; right: 13px; top: 17px;
    display: flex; flex-direction: column; align-items: flex-end; gap: 3px;
  }
  .selling-point {
    background: var(--accent-yellow); color: #111;
    font-size: 15px; font-weight: 600; line-height: 21px; padding: 0 5px;
  }
  .cover-web {
    position: absolute; right: 30px; top: 307px;
    color: var(--text-white); font-size: 12px; font-weight: 400;
  }
  .brand-name {
    position: absolute; left: 117px; top: 452px;
    color: var(--text-white); font-size: 27px; font-weight: 700;
    letter-spacing: 0.5px; white-space: nowrap;
  }
  .fold {
    position: absolute; left: 0; top: 0; width: 24px; height: 100%;
    background: linear-gradient(to right, rgba(0,0,0,0.12), rgba(0,0,0,0));
  }
</style>
</head>
<body>
  <div class="spread">
    <section class="page back-page">
      <div class="info-block hours">
        <p class="info-title">Opening Hours:</p>
        <p class="info-label">MON-FRI</p>
        <p class="info-line">8:00 AM - 5:30 PM</p>
        <p class="info-label">SAT</p>
        <p class="info-line">8.00 AM - 4.00 PM</p>
        <p class="info-note">Out of hours by appointment.</p>
      </div>
      <div class="info-block contact">
        <p class="info-label">Contact us</p>
        <p class="info-small"><span class="detail-key">Phone</span>01236 482915</p>
        <p class="info-small"><span class="detail-key">Email</span>sales@brelwick-example.co.uk</p>
        <p class="info-small"><span class="detail-key">&nbsp;Web</span>www.brelwick-example.co.uk</p>
      </div>
      <div class="info-block location">
        <p class="info-label">Find us at</p>
        <p class="info-small">14 Harlow Place</p>
        <p class="info-small">Kelsmoor Industrial Estate</p>
        <p class="info-small">Cumbernauld G67 9ZZ</p>
      </div>
    </section>

    <section class="page front-page">
      <div class="cover-photo" role="img" aria-label="Black and white photo of a mechanic in a blue shirt lying under a vehicle with tools on the workshop floor"></div>
      <svg class="cover-shapes" width="429" height="605" viewBox="0 0 429 605" aria-hidden="true">
        <polygon points="429,255 429,330 392,330" fill="var(--brand-blue-deep)"/>
        <rect x="0" y="330" width="429" height="8" fill="#2f79e6"/>
        <polygon points="218,338 429,338 429,548 345,605 250,605 368,452" fill="var(--brand-blue-deep)"/>
        <polygon points="429,548 429,605 345,605" fill="#1447b8"/>
      </svg>
      <div class="fold"></div>
      <div class="selling-points">
        <span class="selling-point">Finest customer service</span>
        <span class="selling-point">Quality workmanship</span>
        <span class="selling-point">Competitive prices</span>
      </div>
      <p class="cover-web">www.brelwick-example.co.uk</p>
      <p class="brand-name">BRELWICK MOTORS</p>
    </section>
  </div>
</body>
</html>
```